Rigboard Media Co Business Card Design

We have a newly created business and logo, but we now need business cards using the new logo.
We are an Australian based business, and we sell advertising space on trucks. The business cards will be seen by media buyers, direct advertisers, fleet owners and business people in general.
Our colours are very simple - black and a strong yellow, with some white. We have chosen the black and yellow for various reasons, but in particular because they are high contrast, and they also have a parallel with the number plates used on our roads, which is relevant to our product offering.
My initial thoughts:
Keep it simple and uncluttered
Use both sides
Our default is Century Gothic
I can provide logo files as required. We do not yet have a website, so I can't direct you there just yet. That may well be another project!
Target Market(s)
The business cards will be seen by media buyers, direct advertisers, fleet owners and business people in general.
Industry/Entity Type
Advertising
Look and feel

```html
<!DOCTYPE html>
<html lang="en">
<head>
<meta charset="utf-8">
<title>Rigboard Media Co – Business Card</title>
<link href="https://fonts.googleapis.com/css2?family=Roboto+Condensed:wght@300;400;700&display=swap" rel="stylesheet">
<style>
  :root {
    --bg: #d9d9dc;
    --yellow: #f7ec1f;
    --black: #0a0a0a;
    --ink: #111111;
    --radius: 22px;
  }
  * { box-sizing: border-box; margin: 0; padding: 0; }
  html, body { width: 1200px; height: 960px; overflow: hidden; }
  body {
    background: var(--bg);
    font-family: "Roboto Condensed", Arial, sans-serif;
    display: flex;
    align-items: center;
    justify-content: center;
    gap: 80px;
  }
  .card { border-radius: var(--radius); box-shadow: 0 10px 30px rgba(0,0,0,.18); }

  /* Front */
  .card-front {
    width: 560px; height: 320px;
    background: var(--yellow);
    display: flex; align-items: center; justify-content: center;
  }
  .front-panel {
    width: 440px; height: 210px;
    background: var(--black);
    border-radius: 12px;
    display: flex; align-items: center; justify-content: center;
  }
  .brand-name {
    color: var(--yellow);
    font-weight: 700;
    font-size: 44px;
    letter-spacing: 1px;
    text-transform: uppercase;
  }

  /* Back */
  .card-back {
    width: 320px; height: 560px;
    background: var(--black);
    padding: 40px 34px;
    display: flex; flex-direction: column;
  }
  .back-badge {
    height: 180px;
    border: 7px solid var(--yellow);
    border-radius: 14px;
    display: flex; align-items: center; justify-content: center;
  }
  .back-badge .brand-name { font-size: 26px; }
  .contact { color: var(--yellow); margin-top: 50px; }
  .contact-name { font-weight: 700; font-size: 26px; }
  .contact-role { font-weight: 300; font-size: 18px; margin-bottom: 30px; }
  .contact-line { font-weight: 300; font-size: 16px; line-height: 1.55; }
</style>
</head>
<body>
  <section class="card card-front" aria-label="Card front">
    <div class="front-panel">
      <span class="brand-name">Rigboard Media Co</span>
    </div>
  </section>

  <section class="card card-back" aria-label="Card back">
    <div class="back-badge">
      <span class="brand-name">Rigboard Media Co</span>
    </div>
    <div class="contact">
      <p class="contact-name">Dan Kessler</p>
      <p class="contact-role">Founder</p>
      <p class="contact-line">PO Box 2417</p>
      <p class="contact-line">Harbour Flat NSW 2061</p>
      <p class="contact-line">+61 4 5550 1923</p>
      <p class="contact-line">1800RIGBRD</p>
      <p class="contact-line">dan@rigboard-media.com.au</p>
      <p class="contact-line">www.rigboard-media.com.au</p>
    </div>
  </section>
</body>
</html>
```